hi all

Im after a new age looking business card with my company logo on it

must include these details, I would like the PH and Email to be symbols

If the colours used for card could be kept within the colours used in logo that I have supplied that would be great, if another colour is to be used dark grey would be ok. no light bulbs etc thanks

Details below to be incorporated on card

Damian Holloway

Lic E871302

PH 0219647381

E info@brightvaleelectrical.example.nz

Domestic Commercial Industrial Electricians

```html
<!DOCTYPE html>
<html lang="en">
<head>
<meta charset="utf-8">
<title>Brightvale Electrical — Business Card</title>
<link rel="stylesheet" href="https://fonts.googleapis.com/css2?family=Montserrat:wght@700&family=Open+Sans:wght@400&display=swap">
<style>
  :root {
    --stage: #222428;
    --navy: #28303d;
    --blue: #0f78bf;
    --white: #ffffff;
    --ink: #1e232b;
  }
  * { margin: 0; padding: 0; box-sizing: border-box; }
  html, body {
    width: 1200px; height: 900px; overflow: hidden;
    background: var(--stage);
  }
  .stage { position: relative; width: 1200px; height: 900px; }
  .card {
    position: absolute; left: 285px; width: 630px; height: 360px;
    overflow: hidden; background: var(--white);
    box-shadow: 0 14px 34px rgba(0,0,0,0.45);
  }
  .card--front { top: 75px; }
  .card--back { top: 465px; }
  .card__shapes { position: absolute; inset: 0; }

  .holder-name {
    position: absolute; left: 96px; top: 89px;
    font-family: "Montserrat", sans-serif; font-weight: 700;
    font-size: 24px; letter-spacing: 0.5px; color: var(--white);
    text-transform: uppercase; line-height: 40px; white-space: nowrap;
  }
  .licence {
    position: absolute; left: 160px; top: 180px;
    font-family: "Open Sans", sans-serif; font-size: 20px; color: var(--white);
    word-spacing: 10px; white-space: nowrap;
  }
  .contact {
    position: absolute; left: 70px; display: flex; align-items: center; gap: 14px;
    font-family: "Open Sans", sans-serif; font-size: 15px; color: var(--white);
    white-space: nowrap;
  }
  .contact--phone { top: 250px; }
  .contact--email { top: 302px; }
  .contact__icon { width: 30px; height: 30px; flex: none; }

  .brand {
    position: absolute; display: flex; align-items: center; gap: 10px;
    font-family: "Montserrat", sans-serif; font-weight: 700; color: var(--blue);
    text-transform: uppercase; line-height: 1.05; white-space: nowrap;
  }
  .brand__mark { border-radius: 50%; background: var(--navy); flex: none; }
  .brand--front { left: 452px; top: 120px; font-size: 18px; }
  .brand--front .brand__mark { width: 26px; height: 26px; }
  .brand--back { left: 0; right: 0; top: 62px; justify-content: center; font-size: 32px; }
  .brand--back .brand__mark { width: 42px; height: 42px; }
  .brand__sub { display: block; font-size: 0.5em; letter-spacing: 4px; }

  .tagline {
    position: absolute; left: 0; right: 0; top: 158px; text-align: center;
    font-family: "Open Sans", sans-serif; font-size: 18px; color: var(--ink);
    white-space: nowrap;
  }
</style>
</head>
<body>
<main class="stage">

  <section class="card card--front" aria-label="Business card front">
    <svg class="card__shapes" viewBox="0 0 630 360" width="630" height="360" aria-hidden="true">
      <rect x="0" y="0" width="430" height="360" fill="var(--navy)"/>
      <polygon points="0,68 370,68 425,78 430,150 0,150" fill="var(--blue)"/>
    </svg>
    <div class="holder-name">Damian Holloway</div>
    <div class="licence">LIC: E871302</div>
    <div class="contact contact--phone">
      <svg class="contact__icon" viewBox="0 0 30 30" aria-label="Phone">
        <circle cx="15" cy="15" r="15" fill="var(--white)"/>
        <path d="M10.5 8.5c.7-.5 1.5-.3 1.9.4l1.3 2.2c.4.7.2 1.4-.4 1.8l-.8.5c.6 1.6 1.6 2.8 3.1 3.7l.6-.7c.5-.6 1.2-.7 1.8-.3l2.1 1.4c.7.4.8 1.3.3 1.9l-.9 1.1c-.7.8-1.9 1-3 .5-3.4-1.6-5.8-4.4-7-7.9-.4-1.1 0-2.300.9-3z" fill="var(--ink)"/>
      </svg>
      <span>0219647381</span>
    </div>
    <div class="contact contact--email">
      <svg class="contact__icon" viewBox="0 0 30 30" aria-label="Email">
        <circle cx="15" cy="15" r="15" fill="var(--white)"/>
        <rect x="8" y="10" width="14" height="10" rx="1" fill="var(--ink)"/>
        <path d="M8.5 10.8 15 15.6l6.5-4.8" fill="none" stroke="var(--white)" stroke-width="1.3"/>
      </svg>
      <span>info@brightvaleelectrical.example.nz</span>
    </div>
    <div class="brand brand--front">
      <span class="brand__mark"></span>
      <span>Brightvale<span class="brand__sub">Electrical</span></span>
    </div>
  </section>

  <section class="card card--back" aria-label="Business card back">
    <svg class="card__shapes" viewBox="0 0 630 360" width="630" height="360" aria-hidden="true">
      <polygon points="0,292 230,294 350,294 470,232 630,168 630,360 0,360" fill="var(--navy)"/>
      <polygon points="230,294 350,294 470,232 492,300 315,345" fill="var(--blue)"/>
    </svg>
    <div class="brand brand--back">
      <span class="brand__mark"></span>
      <span>Brightvale<span class="brand__sub">Electrical</span></span>
    </div>
    <p class="tagline">Domestic Commercial Industrial Electricians</p>
  </section>

</main>
</body>
</html>
```